Lotus Bowl take out menu

We need a take out menu design using our menu attached. Info to include would be our address: 5817 Meridel Harrow Pkwy #204, Lafayette, LA 70508. Phone number is 337-614-2953. website is www.lotusbowlvtr.example.

Industry/Entity Type

Asian Restaurant

```html
<!DOCTYPE html>
<html lang="en">
<head>
<meta charset="utf-8">
<title>Lotus Bowl – Take Out Menu</title>
<link href="https://fonts.googleapis.com/css2?family=Permanent+Marker&family=Cinzel:wght@700&family=Open+Sans:wght@400;600;700&display=swap" rel="stylesheet">
<style>
:root{
  --red:#d7191f;
  --ink:#1a1a1a;
  --paper:#ffffff;
  --backdrop:#e9e9e9;
  --muted:#555;
  --photo-a:#8a5a2b;
  --photo-b:#3d2a1a;
  --photo-c:#c49a5c;
}
*{margin:0;padding:0;box-sizing:border-box}
html,body{width:878px;height:1200px;overflow:hidden}
body{background:var(--backdrop);font-family:'Open Sans',sans-serif;color:var(--ink);position:relative}
.page{position:absolute;width:368px;height:555px;background:var(--paper);overflow:hidden;box-shadow:0 2px 6px rgba(0,0,0,.18)}
.page--cover{left:58px;top:29px}
.page--story{left:452px;top:29px}
.page--appetizers{left:58px;top:630px}
.page--entrees{left:452px;top:630px}

.ring{position:absolute;border-radius:50%;border:22px solid var(--red);}
.photo{position:absolute;border-radius:50%;background:radial-gradient(circle at 40% 40%,var(--photo-c),var(--photo-a) 55%,var(--photo-b));}

.brand{position:absolute;left:0;right:0;top:382px;text-align:center}
.brand__row{display:flex;align-items:center;justify-content:center;gap:8px}
.brand__dot{width:22px;height:22px;border-radius:50%;background:var(--red)}
.brand__name{font-family:'Cinzel',serif;font-weight:700;font-size:38px;letter-spacing:1px;color:var(--ink)}
.brand__tag{font-family:'Cinzel',serif;font-weight:700;font-size:11px;letter-spacing:3px;color:var(--red);margin-top:2px}

.contact{position:absolute;left:0;right:0;bottom:30px;text-align:center;font-size:7px;line-height:1.5;color:var(--red)}

.mark{position:absolute;background:var(--ink)}
.mark--square{left:44px;top:22px;width:44px;height:44px}
.mark--circle{left:30px;top:22px;width:56px;height:56px;border-radius:50%}

.heading{position:absolute;left:34px;top:140px;font-family:'Permanent Marker',sans-serif;font-size:30px;color:var(--red);letter-spacing:1px}

.story{position:absolute;left:34px;right:34px;top:192px;font-size:7.2px;line-height:1.6;color:var(--muted)}
.story p{margin-bottom:9px}

.menu{position:absolute;left:30px;right:26px;top:186px;display:grid;grid-template-columns:1fr 1fr;column-gap:18px}
.item{margin-bottom:15px}
.item__head{display:flex;justify-content:space-between;font-size:7.5px;font-weight:700;color:var(--ink)}
.item__price{color:var(--ink)}
.item__desc{font-size:6px;line-height:1.4;color:var(--muted);margin-top:1px}
.spicy{color:var(--red)}
.subhead{background:var(--ink);color:var(--paper);font-size:7px;font-weight:700;letter-spacing:1.5px;text-align:center;padding:2px 0;margin:2px 0 12px}
</style>
</head>
<body>

<section class="page page--cover">
  <div class="ring" style="left:-20px;top:-60px;width:400px;height:400px"></div>
  <div class="photo" style="left:30px;top:-10px;width:300px;height:300px" role="img" aria-label="Photo of stir-fried noodles, spring rolls and vegetable dishes"></div>
  <div class="brand">
    <div class="brand__row"><span class="brand__dot"></span><span class="brand__name">LOTUS BOWL</span></div>
    <div class="brand__tag">FRESH ASIAN CUISINE</div>
  </div>
  <div class="contact">5817 Meridel Harrow Pkwy #204, Lafayette, LA 70508<br>Ph: 337-614-2953 &nbsp;·&nbsp; www.lotusbowlvtr.example</div>
</section>

<section class="page page--story">
  <div class="mark mark--square"></div>
  <div class="ring" style="left:222px;top:-50px;width:180px;height:180px;border-width:16px"></div>
  <div class="photo" style="left:240px;top:-32px;width:144px;height:144px" role="img" aria-label="Photo of a grilled meat dish with vegetables"></div>
  <h2 class="heading">OUR STORY</h2>
  <div class="story">
    <p>At Lotus Bowl, we take pride in serving fresh, authentic Asian dishes made with care from recipes passed down through our family for generations.</p>
    <p>Our kitchen blends traditional flavors from across Asia with local ingredients, and every plate is cooked to order so it arrives hot, crisp and full of flavor.</p>
    <p>Our founders first opened the doors with a simple dream: to share the food they grew up with and to welcome every guest like a member of the family.</p>
    <p>Whether you dine in or take out, we hope each meal brings you comfort, warmth and a reason to return soon.</p>
  </div>
  <div class="contact">5817 Meridel Harrow Pkwy #204, Lafayette, LA 70508<br>Ph: 337-614-2953 &nbsp;·&nbsp; www.lotusbowlvtr.example</div>
</section>

<section class="page page--appetizers">
  <div class="mark mark--circle"></div>
  <div class="ring" style="left:205px;top:-60px;width:200px;height:200px;border-width:18px"></div>
  <div class="photo" style="left:225px;top:-40px;width:160px;height:160px" role="img" aria-label="Photo of fried appetizers on a plate"></div>
  <h2 class="heading">APPETIZERS</h2>
  <div class="menu">
    <div>
      <div class="item"><div class="item__head"><span>Edamame</span><span class="item__price">4.95</span></div><div class="item__desc">Steamed soybeans with sea salt</div></div>
      <div class="item"><div class="item__head"><span>Spring Rolls (2)</span><span class="item__price">3.95</span></div><div class="item__desc">Crispy vegetable rolls, sweet chili sauce</div></div>
      <div class="item"><div class="item__head"><span>Crab Rangoon (6)</span><span class="item__price">5.95</span></div><div class="item__desc">Cream cheese and crab in crisp wonton</div></div>
      <div class="item"><div class="item__head"><span>Pot Stickers (6)</span><span class="item__price">5.95</span></div><div class="item__desc">Pan fried pork dumplings, ginger soy</div></div>
      <div class="item"><div class="item__head"><span>Chicken Satay</span><span class="item__price">6.95</span></div><div class="item__desc">Grilled skewers with peanut sauce</div></div>
      <div class="item"><div class="item__head"><span>Lettuce Wraps</span><span class="item__price">7.95</span></div><div class="item__desc">Minced chicken, water chestnut, hoisin</div></div>
      <div class="item"><div class="item__head"><span>Tempura Shrimp</span><span class="item__price">7.95</span></div><div class="item__desc">Light batter, tempura dipping sauce</div></div>
      <div class="item"><div class="item__head"><span>Sampler Platter</span><span class="item__price">9.95</span></div><div class="item__desc">Rolls, rangoon, satay and dumplings</div></div>
    </div>
    <div>
      <div class="item"><div class="item__head"><span>Salt &amp; Pepper Calamari</span><span class="item__price">7.95</span></div><div class="item__desc">Tossed with jalapeño and scallion</div></div>
      <div class="item"><div class="item__head"><span>Crispy Tofu</span><span class="item__price">5.95</span></div><div class="item__desc">Golden cubes with sweet soy glaze</div></div>
      <div class="item"><div class="item__head"><span>Fried Chicken Wings</span><span class="item__price">6.95</span></div><div class="item__desc">Garlic butter or spicy honey</div></div>
      <div class="item"><div class="item__head"><span>Wonton Soup</span><span class="item__price">3.95</span></div><div class="item__desc">Pork wontons in clear broth</div></div>
      <div class="item"><div class="item__head"><span>Hot &amp; Sour Soup <span class="spicy">●</span></span><span class="item__price">3.95</span></div><div class="item__desc">Tofu, mushroom, bamboo shoots</div></div>
      <div class="item"><div class="item__head"><span>Vegetable Spring Rolls</span><span class="item__price">4.95</span></div><div class="item__desc">Fresh herbs, rice paper, peanut dip</div></div>
      <div class="item"><div class="item__head"><span>Miso Soup</span><span class="item__price">2.95</span></div><div class="item__desc">Tofu, seaweed and green onion</div></div>
      <div class="item"><div class="item__head"><span>House Salad</span><span class="item__price">3.95</span></div><div class="item__desc">Mixed greens with ginger dressing</div></div>
    </div>
  </div>
</section>

<section class="page page--entrees">
  <div class="mark mark--circle"></div>
  <div class="ring" style="left:205px;top:-60px;width:200px;height:200px;border-width:18px"></div>
  <div class="photo" style="left:225px;top:-40px;width:160px;height:160px" role="img" aria-label="Photo of a shrimp and vegetable entree"></div>
  <h2 class="heading">ENTREES</h2>
  <div class="menu">
    <div>
      <div class="item"><div class="item__head"><span>General Tso Chicken <span class="spicy">●</span></span><span class="item__price">10.95</span></div><div class="item__desc">Crispy chicken in tangy chili glaze</div></div>
      <div class="item"><div class="item__head"><span>Sesame Chicken</span><span class="item__price">10.95</span></div><div class="item__desc">Sweet sauce topped with sesame seeds</div></div>
      <div class="item"><div class="item__head"><span>Orange Chicken</span><span class="item__price">10.95</span></div><div class="item__desc">Fresh orange zest and citrus sauce</div></div>
      <div class="item"><div class="item__head"><span>Kung Pao Shrimp <span class="spicy">●</span></span><span class="item__price">12.95</span></div><div class="item__desc">Peanuts, peppers and dried chili</div></div>
      <div class="item"><div class="item__head"><span>Mongolian Beef</span><span class="item__price">12.95</span></div><div class="item__desc">Flank steak with scallion and onion</div></div>
      <div class="item"><div class="item__head"><span>Broccoli Beef</span><span class="item__price">11.95</span></div><div class="item__desc">Tender beef in savory brown sauce</div></div>
      <div class="item"><div class="item__head"><span>Sweet &amp; Sour Pork</span><span class="item__price">10.95</span></div><div class="item__desc">Pineapple, peppers and onion</div></div>
      <div class="item"><div class="item__head"><span>Ma Po Tofu <span class="spicy">●</span></span><span class="item__price">9.95</span></div><div class="item__desc">Silken tofu in spicy bean sauce</div></div>
    </div>
    <div>
      <div class="item"><div class="item__head"><span>Pad Thai</span><span class="item__price">11.95</span></div><div class="item__desc">Rice noodles, egg, peanuts, lime</div></div>
      <div class="item"><div class="item__head"><span>Drunken Noodles <span class="spicy">●</span></span><span class="item__price">11.95</span></div><div class="item__desc">Wide noodles with basil and chili</div></div>
      <div class="subhead">RICE &amp; NOODLES</div>
      <div class="item"><div class="item__head"><span>House Fried Rice</span><span class="item__price">9.95</span></div><div class="item__desc">Chicken, shrimp, pork and egg</div></div>
      <div class="item"><div class="item__head"><span>Vegetable Lo Mein</span><span class="item__price">8.95</span></div><div class="item__desc">Soft noodles with seasonal greens</div></div>
      <div class="item"><div class="item__head"><span>Singapore Noodles</span><span class="item__price">10.95</span></div><div class="item__desc">Curry rice vermicelli and shrimp</div></div>
      <div class="item"><div class="item__head"><span>Teriyaki Salmon</span><span class="item__price">14.95</span></div><div class="item__desc">Grilled fillet with steamed rice</div></div>
      <div class="item"><div class="item__head"><span>Beef Chow Fun</span><span class="item__price">11.95</span></div><div class="item__desc">Flat noodles, bean sprouts, onion</div></div>
    </div>
  </div>
</section>

</body>
</html>
```